Yacht Management in Miami & Ft Lauderdale (2019Q2)

I’m looking for a flyer to leave places for people to get information about my company and what services we offer.
We offer monthly management plans to ensure the vessel is ready to go at a moments notice. This can be as simple as washing once a week, or as involved as washing, waxing, detailing, provisioning, and crew services.
We also offer bespoke customizations; stereos, on board WiFi, and engineering.

Target Market(s)

Yacht and boat owners.

Font styles to use
Sans Serif

Colors
87d0c7
85cae6
85acd3
cedeed
cee9f5
cfeae6
0455a3

Requirements
Must have
• Must have simple attention grabbing, without being obnoxious.
• Prefer a 3in x 5in post card size. other size may be an option.
• Must be front and back.
Nice to have
• Languages: English, Spanish, Russian
• USA flag logo
Should not have
• Should not have a lot of text. Icons and photos are great.

```html
<!DOCTYPE html>
<html lang="en">
<head>
<meta charset="utf-8">
<title>Harbor Sage – Postcard Front and Back</title>
<link href="https://fonts.googleapis.com/css2?family=Oswald:wght@300;400;600&family=Open+Sans:wght@400&display=swap" rel="stylesheet">
<style>
  :root {
    --page: #ffffff;
    --red-top: #c92a10;
    --red-bottom: #e4232c;
    --accent-red: #e4232c;
    --ink: #ffffff;
    --mark: #111111;
    --label: #333333;
    --night-sky: #2c3446;
    --night-mid: #4a5260;
    --night-water: #0f1a18;
    --night-glow: #3fc24d;
    --dusk-sky: #6f7479;
    --dusk-sun: #e49a3a;
    --dusk-sea: #2d2c2c;
  }
  * { box-sizing: border-box; margin: 0; padding: 0; }
  html, body { width: 1200px; height: 720px; overflow: hidden; background: var(--page); }
  body { position: relative; font-family: "Oswald", "Arial Narrow", sans-serif; font-weight: 300; color: var(--ink); }

  .card { position: absolute; top: 151px; height: 356px; box-shadow: 1px 2px 4px rgba(0,0,0,.25); background: var(--page); }
  .card--front { left: 34px; width: 550px; }
  .card--back { left: 610px; width: 550px; }

  .red-panel { position: absolute; top: 0; width: 153px; height: 100%;
    background: linear-gradient(180deg, var(--red-top), var(--red-bottom)); }
  .card--front .red-panel { left: 0; }
  .card--back .red-panel { right: 0; }

  .photo { position: absolute; top: 0; height: 100%; width: 395px; }
  .card--front .photo { right: 0;
    background:
      radial-gradient(ellipse 60% 22% at 45% 84%, rgba(63,194,77,.85), rgba(63,194,77,0) 70%),
      linear-gradient(180deg, var(--night-sky) 0%, var(--night-mid) 45%, #6d7480 62%, #1f2326 72%, var(--night-water) 100%); }
  .card--back .photo { left: 0;
    background:
      radial-gradient(ellipse 30% 20% at 5% 52%, rgba(248,190,80,.9), rgba(248,190,80,0) 70%),
      linear-gradient(180deg, #5d6672 0%, var(--dusk-sky) 30%, #a38a72 45%, var(--dusk-sun) 53%, #6a5848 57%, var(--dusk-sea) 66%, #585a5e 80%, #8a8c8e 100%); }

  .headline { position: absolute; left: 0; width: 100%; top: 30px; text-align: center;
    font-size: 34px; line-height: 34px; font-weight: 300; letter-spacing: -0.5px; }

  .brand-mark { position: absolute; left: 0; width: 100%; text-align: center;
    color: var(--mark); font-weight: 600; font-size: 24px; line-height: 24px; text-transform: uppercase; }
  .card--front .brand-mark, .card--back .brand-mark { top: 412px; top: 412px; }
  .brand-mark { top: 258px; }

  .service-list { position: absolute; left: 23px; top: 32px; width: 360px;
    font-size: 15.5px; line-height: 18px; text-transform: uppercase; letter-spacing: -0.1px; }
  .service-list .sep { color: var(--accent-red); padding: 0 3px; }

  .services { position: absolute; left: 20px; top: 22px; width: 357px;
    display: grid; grid-template-columns: repeat(3, 119px); row-gap: 10px; }
  .service { text-align: center; }
  .service svg { display: block; margin: 0 auto 2px; width: 16px; height: 16px; }
  .service h3 { font-weight: 600; font-size: 6.6px; line-height: 9px; text-transform: uppercase; }
  .service p { font-size: 6px; line-height: 9.5px; }

  .contact { position: absolute; left: 0; width: 100%; text-align: center; }
  .contact h2 { font-weight: 300; font-size: 19px; line-height: 20px; margin-top: 22px; text-transform: uppercase; }
  .contact .web { font-size: 12px; margin-top: 42px; }
  .contact .line { font-size: 8.5px; line-height: 12.5px; }
  .contact .address { margin-top: 4px; }

  .side-labels { position: absolute; top: 673px; left: 0; width: 100%; height: 24px;
    font-family: "Open Sans", Arial, sans-serif; color: var(--label); font-size: 11px; }
  .side-labels span { position: absolute; top: 5px; }
  .side-labels .front { right: 612px; }
  .side-labels .back { left: 611px; }
  .side-labels .divider { position: absolute; left: 597px; top: 0; width: 1px; height: 24px; background: var(--label); }
</style>
</head>
<body>

<section class="card card--front">
  <div class="red-panel">
    <h1 class="headline">YACHT<br>SERVICE<br>YOU CAN<br>TRUST</h1>
    <div class="brand-mark">Harbor<br>Sage</div>
  </div>
  <div class="photo" role="img" aria-label="Photo of a motor yacht moored at a dock at dusk with green underwater lights and city lights behind">
    <p class="service-list">
      Fair and friendly complete yacht service<span class="sep">|</span>Monthly management plans<span class="sep">|</span>Bespoke refits, updates and customizations<span class="sep">|</span>Engineering<span class="sep">|</span>Stereo systems and on-board Wi-Fi<span class="sep">|</span>Captaining and crew<span class="sep">|</span>Internet sales
    </p>
  </div>
</section>

<section class="card card--back">
  <div class="photo" role="img" aria-label="Photo of a yacht foredeck looking out over calm sea at sunset">
    <div class="services">
      <div class="service">
        <svg viewBox="0 0 16 16" fill="none" stroke="#fff" stroke-width="1.4"><circle cx="8" cy="2.5" r="1.4"/><path d="M8 4v10M5 6.5h6M2.5 9.5c0 2.5 2.5 4.5 5.5 4.5s5.5-2 5.5-4.5"/></svg>
        <h3>Complete Yacht Service</h3>
        <p>Monthly management plans to<br>ensure your vessel is ready to<br>go at a moment's notice.</p>
      </div>
      <div class="service">
        <svg viewBox="0 0 16 16" fill="#fff"><rect x="5" y="1.5" width="6" height="13" rx="1"/><circle cx="8" cy="10" r="2" fill="#6f7479"/><circle cx="8" cy="4.5" r="1" fill="#6f7479"/><path d="M3 5c-1 2-1 4 0 6M13 5c1 2 1 4 0 6" stroke="#fff" fill="none" stroke-width="1.2"/></svg>
        <h3>Stereo Packages</h3>
        <p>From mild to wild. For DIY or with full<br>installation, we can tailor a stereo<br>package for your vessel and your desires.</p>
      </div>
      <div class="service">
        <svg viewBox="0 0 16 16"><circle cx="8" cy="8" r="5" fill="none" stroke="#fff" stroke-width="3" stroke-dasharray="2.2 1.7"/><circle cx="8" cy="8" r="4.2" fill="none" stroke="#fff" stroke-width="1.6"/></svg>
        <h3>Troubleshooting</h3>
        <p>With experience on every major<br>brand and many bespoke brands,<br>we are able to diagnose most issues.</p>
      </div>
      <div class="service">
        <svg viewBox="0 0 16 16" fill="#fff"><rect x="6.5" y="1" width="3" height="3"/><rect x="4" y="4" width="8" height="4" rx="1"/><path d="M1.5 8h13l-2 6h-9z"/></svg>
        <h3>Bespoke Refits and Updates</h3>
        <p>Audio-visual and internet services,<br>from TVs on custom lifts and<br>fold outs, to on-board wi-fi, we<br>perform most projects in-house<br>from design to installation.</p>
      </div>
      <div class="service">
        <svg viewBox="0 0 16 16" fill="none" stroke="#fff" stroke-width="1.3"><ellipse cx="8" cy="8" rx="7" ry="4.5"/><path d="M2 9.5h12"/><circle cx="8" cy="6.5" r="1.2" fill="#fff"/></svg>
        <h3>Captaining and Crew</h3>
        <p>Having crew on board is one of<br>the most relaxing parts of owning<br>a yacht. With our Captain, Mate<br>and Stewardess services we can ensure<br>your every need is taken care of.</p>
      </div>
      <div class="service">
        <svg viewBox="0 0 16 16" fill="none" stroke="#fff" stroke-width="1.3"><rect x="1" y="1.5" width="14" height="10"/><path d="M5 15h6M8 11.5V15M5.5 6.5l2 2 3.5-4"/></svg>
        <h3>Internet Sales</h3>
        <p>If you're a DIY person we offer packages<br>to install an A/C pump, stereo, Tabio<br>wall control, Aurel, LED lighting and<br>more. We can even help you out over<br>the phone if you hit a roadblock.</p>
      </div>
    </div>
  </div>
  <div class="red-panel">
    <div class="contact">
      <h2>Contact us today<br>to find out more</h2>
      <p class="web">harborsage.us</p>
      <p class="line" style="margin-top:6px">call: (954) 555-0142</p>
      <p class="line">email: hello@harborsage.us</p>
      <p class="line address">2840 Bayview Drive, #210<br>Miami Beach, FL 33140</p>
    </div>
    <div class="brand-mark">Harbor<br>Sage</div>
  </div>
</section>

<div class="side-labels">
  <span class="front">FRONT</span>
  <div class="divider"></div>
  <span class="back">BACK</span>
</div>

</body>
</html>
```